Natural Medicine & Health/Fitness Coaching studio requires web page

Require a innovative web page for a studio that coaches clients to better health, nutrition and fitness. The studio compromises of Clinical Nutritionists, Naturopaths, Rehab Trainers, Personal Trainers and Sport Coaches. Would like to see earthy but bold designs emphasizing nutritional health and athletic performance.
Updates

Design only launched today.

Target Market(s)

All genders from 20's to 60's, as well as families

Industry/Entity Type

Nutritionist

Coding

Coded - Design and coding required

Number of Pages Required

3 page

Colors
abd037
3277b5
fbee3d
fece3e
33b8a4
f04a50

Requirements
Must have
• Online booking system, ability to message
• Home page
• Coaching/Fitness page
• Nutritional Medicine page
• Must be suitable for both Fitness and Nutrition

```html
<!DOCTYPE html>
<html lang="en">
<head>
<meta charset="utf-8">
<title>Vital Stride – Nutritional Therapy</title>
<link href="https://fonts.googleapis.com/css2?family=Lato:wght@400;700;900&display=swap" rel="stylesheet">
<style>
:root{
  --green:#a3c62f;
  --blue:#2f62a8;
  --teal:#2fae98;
  --red:#ec3a47;
  --yellow:#fbc02d;
  --ink:#333;
  --grey:#f1f1f1;
  --heading:#1f5a9e;
}
*{margin:0;padding:0;box-sizing:border-box}
html,body{width:1200px;height:4110px;overflow:hidden}
body{position:relative;background:#fff;font-family:'Lato',sans-serif;color:var(--ink)}
.abs{position:absolute}
.topline{left:0;top:0;width:1200px;height:8px;background:var(--teal)}
.call{left:836px;top:0;width:288px;height:54px;background:var(--red);color:#fff;font-weight:700;font-size:17px;display:flex;align-items:center;justify-content:center;gap:10px;clip-path:polygon(4% 0,100% 0,96% 100%,0 100%)}
.brand{left:77px;top:32px;font-size:50px;font-weight:700;color:var(--green);display:flex;align-items:center;gap:10px;line-height:1}
.brand .dot{width:26px;height:26px;border-radius:50%;background:var(--blue)}
.nav{left:525px;top:86px;display:flex;gap:44px;font-size:14px;font-weight:700;color:#222}
.nav .on{color:var(--blue)}
.hero{left:0;top:129px;width:1200px;height:556px;background:linear-gradient(120deg,#2e6a2c,#4f8f3c 55%,#3a7430)}
.hero-tag{left:77px;top:351px;width:356px;height:120px;background:var(--green);color:#fff;padding:10px 14px}
.hero-tag h1{font-size:34px;font-weight:900;line-height:1.15}
.hero-tag p{font-size:18px;color:#222;font-weight:700}
.wave{left:0;top:620px}
.sec-title{width:1200px;text-align:center;font-size:34px;font-weight:900;color:var(--heading)}
.welcome-text{left:160px;top:812px;width:880px;text-align:center;font-size:14.5px;line-height:1.9}
.btn{display:flex;align-items:center;justify-content:center;color:#fff;font-weight:700;font-size:15px}
.btn-green{background:var(--green)}
.btn-blue{background:var(--blue)}
.grey{left:0;top:1049px;width:1200px;height:1288px;background:var(--grey)}
.photo{position:absolute}
.panel{position:absolute;color:#fff;padding:28px 60px}
.panel h3{font-size:32px;font-weight:900;margin-bottom:12px}
.panel p{font-size:14px;line-height:1.7}
.panel.right{text-align:right}
.panel .btn{position:absolute;width:180px;height:50px}
.badge{position:absolute;height:110px}
.booking-photo{left:0;top:2625px;width:575px;height:485px;background:linear-gradient(135deg,#c7b7a8,#d9475c 50%,#8a6a5a)}
.booking{left:520px;top:2658px;width:680px;height:411px;background:linear-gradient(135deg,var(--teal),#2b8aa6);clip-path:polygon(6% 0,100% 0,100% 100%,0 100%);color:#fff}
.booking h2{position:absolute;left:94px;top:52px;font-size:34px;font-weight:900}
.field{position:absolute;background:#fff;color:#555;font-size:13px;padding:10px 12px}
.quote{left:420px;top:3270px;width:610px;font-size:15px;line-height:1.8}
.quote .by{margin-top:16px;font-size:20px;font-weight:700}
.news-band{left:0;top:3543px;width:1200px;height:137px;background:linear-gradient(90deg,var(--red) 35%,#9a5f6c 60%,var(--teal))}
.news-box{left:77px;top:3521px;width:356px;height:179px;background:var(--teal);clip-path:polygon(0 0,100% 0,92% 100%,0 100%);color:#fff;font-size:34px;font-weight:900;text-align:center;line-height:1.1;display:flex;align-items:center;justify-content:center}
.foot h4{font-size:18px;font-weight:900;color:var(--heading);margin-bottom:22px}
.foot ul{list-style:none;font-size:14px;line-height:2}
.contact li{display:flex;gap:12px;align-items:flex-start;line-height:1.7;margin-bottom:6px}
.copy{left:0;top:4041px;width:1200px;height:69px;background:var(--grey);font-size:13px;display:flex;align-items:center;justify-content:center}
</style>
</head>
<body>
<div class="abs topline"></div>
<div class="abs call"><svg width="16" height="16" viewBox="0 0 24 24"><path fill="#fff" d="M6.6 10.8a15 15 0 0 0 6.6 6.6l2.2-2.2c.3-.3.7-.4 1-.2 1.1.4 2.3.6 3.6.6.6 0 1 .4 1 1V20c0 .6-.4 1-1 1A17 17 0 0 1 3 4c0-.6.4-1 1-1h3.5c.6 0 1 .4 1 1 0 1.3.2 2.5.6 3.6.1.3 0 .7-.2 1z"/></svg>CALL US: 1-800-555-0142</div>
<div class="abs brand"><span class="dot"></span>Vital Stride</div>
<nav class="abs nav"><span class="on">HOME</span><span>ABOUT US</span><span>COACHING</span><span>FITNESS</span><span>NUTRITION</span><span>CONTACT US</span></nav>

<div class="abs hero" role="img" aria-label="Woman holding fresh leafy greens and a dumbbell against a green wall"></div>
<div class="abs hero-tag"><h1>Vital Stride<br>Nutritional Therapy</h1><p>Nutritional Therapy</p></div>
<svg class="abs wave" width="1200" height="80" viewBox="0 0 1200 80"><path d="M0 30 Q600 95 1200 20 L1200 80 L0 80Z" fill="var(--red)"/><path d="M0 45 Q600 105 1200 42 L1200 80 L0 80Z" fill="#fff"/></svg>

<h2 class="abs sec-title" style="left:0;top:752px">WELCOME TO OUR WEBSITE</h2>
<p class="abs welcome-text">Lorem ipsum dolor sit amet, consectetur adipiscing elit. Etiam mattis sodales risus, non rhoncus est gravida id. Fusce mattis ligula at enim lacinia, quis luctus lacus aliquet. Sed ac tempor nibh. Donec auctor tortor aliquam ligula fringilla ullamcorper. Phasellus id lacus ipsum. Morbi porttitor lectus purus, nec vulputate nisl convallis et.</p>
<div class="abs btn btn-green" style="left:510px;top:926px;width:180px;height:49px">READ MORE</div>

<div class="abs grey"></div>
<h2 class="abs sec-title" style="left:0;top:1102px">WHAT WE DO</h2>

<div class="photo" style="left:77px;top:1181px;width:600px;height:326px;background:linear-gradient(135deg,#e9e4dc,#cfd6c8 60%,#b9872f)" role="img" aria-label="Smiling nutritionist with vegetables in a bright office"></div>
<div class="panel" style="left:526px;top:1206px;width:598px;height:274px;background:var(--green);clip-path:polygon(0 0,100% 0,100% 100%,5% 100%,8% 50%)">
  <h3>NUTRITION</h3><p>Lorem ipsum dolor sit amet, consectetur adipiscing elit. Etiam mattis sodales risus, non rhoncus est gravida id. Fusce mattis ligula at enim lacinia, quis luctus lacus aliquet. Sed ac tempor nibh. Donec auctor tortor aliquam ligula fringilla ullamcorper.</p>
  <div class="btn btn-blue" style="left:396px;top:196px">READ MORE</div></div>

<div class="photo" style="left:526px;top:1556px;width:598px;height:326px;background:linear-gradient(135deg,#4a5560,#8b8f92 50%,#3b3f44)" role="img" aria-label="People training with kettlebells in a gym"></div>
<div class="panel right" style="left:77px;top:1581px;width:600px;height:274px;background:var(--red);clip-path:polygon(0 0,100% 0,92% 50%,95% 100%,0 100%)">
  <h3>FITNESS</h3><p>Lorem ipsum dolor sit amet, consectetur adipiscing elit. Etiam mattis sodales risus, non rhoncus est gravida id. Fusce mattis ligula at enim lacinia, quis luctus lacus aliquet. Sed ac tempor nibh. Donec auctor tortor aliquam ligula fringilla ullamcorper.</p>
  <div class="btn btn-blue" style="left:25px;top:196px">READ MORE</div></div>

<div class="photo" style="left:77px;top:1929px;width:600px;height:326px;background:linear-gradient(135deg,#2f4a2a,#6b7a4c 55%,#3f4a3a)" role="img" aria-label="Two runners jogging on a tree-lined park path"></div>
<div class="panel" style="left:526px;top:1954px;width:598px;height:274px;background:var(--teal);clip-path:polygon(0 0,100% 0,100% 100%,5% 100%,8% 50%)">
  <h3>COACHING</h3><p>Lorem ipsum dolor sit amet, consectetur adipiscing elit. Etiam mattis sodales risus, non rhoncus est gravida id. Fusce mattis ligula at enim lacinia, quis luctus lacus aliquet. Sed ac tempor nibh. Donec auctor tortor aliquam ligula fringilla ullamcorper.</p>
  <div class="btn btn-blue" style="left:396px;top:196px">READ MORE</div></div>

<h2 class="abs sec-title" style="left:0;top:2394px;font-size:24px;color:#111">OUR PARTNERS</h2>
<div class="badge" style="left:320px;top:2452px;width:290px;background:#222;clip-path:polygon(6% 0,100% 0,94% 100%,0 100%)"></div>
<div class="badge" style="left:640px;top:2452px;width:250px;background:var(--blue);clip-path:polygon(12% 0,100% 0,88% 100%,0 100%)"></div>

<div class="abs booking-photo" role="img" aria-label="Smiling woman using a laptop in a kitchen"></div>
<div class="abs booking">
  <h2>ONLINE BOOKING</h2>
  <div class="field" style="left:94px;top:128px;width:248px;height:42px">Name</div>
  <div class="field" style="left:94px;top:180px;width:248px;height:42px">Email Addres</div>
  <div class="field" style="left:94px;top:232px;width:248px;height:42px">Phone</div>
  <div class="field" style="left:356px;top:128px;width:248px;height:146px">Message</div>
  <div class="btn btn-green" style="position:absolute;left:426px;top:288px;width:178px;height:50px">SUBMIT</div>
</div>

<h2 class="abs sec-title" style="left:0;top:3178px">TESTIMONIALS</h2>
<div class="abs" style="left:178px;top:3260px;width:192px;height:192px;border-radius:50%;border:5px solid var(--red);background:linear-gradient(135deg,#e8d6c8,#b98a72)" role="img" aria-label="Portrait of a smiling client"></div>
<div class="abs quote">“Sed ut perspiciatis unde omnis iste natus error sit voluptatem accusantium doloremque laudantium, totam rem aperiam, eaque ipsa quae ab illo inventore veritatis et quasi architecto beatae vitae dicta sunt explicabo. Nemo enim ipsam voluptatem quia voluptas sit aspernatur aut odit aut fugit, sed quia consequuntur magni dolores eos”<div class="by">- Anaya</div></div>

<div class="abs news-band"></div>
<div class="abs news-box">NEWSLETTER<br>SIGN UP</div>
<div class="abs field" style="left:452px;top:3589px;width:474px;height:50px;padding:16px 14px">Enter Email Addres</div>
<div class="abs btn" style="left:940px;top:3589px;width:184px;height:50px;background:var(--yellow);font-size:14px">SUBSCRIBE NOW</div>

<div class="abs foot" style="left:104px;top:3765px"><h4>QUICK LINKS</h4><ul><li>Home</li><li>About us</li><li>Coaching</li><li>Fitness</li><li>Nutrition</li><li>Contact us</li></ul></div>
<div class="abs foot contact" style="left:375px;top:3765px"><h4>CONTACT US</h4><ul>
<li><svg width="14" height="18" viewBox="0 0 24 30"><path d="M12 0a10 10 0 0 0-10 10c0 8 10 20 10 20s10-12 10-20A10 10 0 0 0 12 0zm0 14a4 4 0 1 1 0-8 4 4 0 0 1 0 8z" fill="#222"/></svg><span>42 Fernhill Lane,<br>Glasgow, G12 7QX</span></li>
<li><svg width="14" height="14" viewBox="0 0 24 24"><path fill="#222" d="M6.6 10.8a15 15 0 0 0 6.6 6.6l2.2-2.2c.3-.3.7-.4 1-.2 1.1.4 2.3.6 3.6.6.6 0 1 .4 1 1V20c0 .6-.4 1-1 1A17 17 0 0 1 3 4c0-.6.4-1 1-1h3.5c.6 0 1 .4 1 1 0 1.3.2 2.5.6 3.6.1.3 0 .7-.2 1z"/></svg>1-800-555-0142</li>
<li><svg width="14" height="14" viewBox="0 0 24 24"><rect x="2" y="5" width="20" height="14" fill="#222"/><path d="M2 5l10 8 10-8" stroke="#fff" stroke-width="2" fill="none"/></svg>hello@vitalstride.com</li>
</ul>
<div style="display:flex;gap:16px;margin-top:16px"><span style="width:14px;height:14px;border-radius:50%;background:#333"></span><span style="width:14px;height:14px;border-radius:50%;background:#333"></span><span style="width:14px;height:14px;border-radius:50%;background:#333"></span><span style="width:14px;height:14px;border-radius:50%;background:#333"></span><span style="width:14px;height:14px;border-radius:50%;background:#333"></span></div></div>
<div class="abs" style="left:633px;top:3770px;width:491px;height:230px;background:linear-gradient(135deg,#dfe8d6,#e9e6dc 50%,#cfdccb);border:3px solid #ccc" role="img" aria-label="Street map showing the studio location in Glasgow"></div>

<div class="abs copy">Copyright © 2019. Company Name All Rights Reserved.</div>
</body>
</html>
```